out of the box Business Card Design for a Manufacturer / Distributor

We are a manufarturer and distributor of products.
the company name is VORTANI (Pic attached)

the picture is NOT a must have on the business Card.

the Business Card should look really professional and/or special, so out of the box thinking is welcome.

there should be 2 Adresses on the Business Card for Main and Branch Office.
Email Adress, homepage, Name is required
NO Phone Number

Our working field:
Private Labeling
high Quality Production
direct distribution
warehousing
trademark registration
legal support

Main Office:
Kornblumenweg 14
08352 Burgstädt
Austria

Branch Office:
Daska Lane
Karvanpur
Malaysia

Names:
Lukas Feldhaus (Owner)
Imran Qureshi (Owner)

Email:
lukas@vortani-example.com
imran@vortani-example.com

homepage:
vortani-example.com

Industry/Entity Type

Manufacturer Distributer

Contact Information for Business Card

Vortani

Requirements
Must have
• Names, both office Adresses, email, homepage
Should not have
• Phone Number

```html
<!DOCTYPE html>
<html lang="en">
<head>
<meta charset="utf-8">
<title>Vortani Business Card</title>
<link rel="stylesheet" href="https://fonts.googleapis.com/css2?family=Lato:wght@700&family=Rubik:ital,wght@0,400;0,500;1,400&display=swap">
<style>
  :root {
    --brand-red: #d40000;
    --brand-crimson: #b0003a;
    --brand-purple: #7a0080;
    --ink: #111111;
    --card-edge: #bdbdbd;
    --paper: #ffffff;
  }
  * { margin: 0; padding: 0; box-sizing: border-box; }
  html, body {
    width: 1200px; height: 1000px; overflow: hidden;
    background: var(--paper);
    font-family: "Rubik", sans-serif;
    color: var(--ink);
  }
  .card {
    position: absolute; left: 252px; top: 275px;
    width: 696px; height: 449px;
    border: 1px solid var(--card-edge);
    background: var(--paper);
    overflow: hidden;
  }
  .card-header { position: absolute; left: 0; top: 0; width: 696px; height: 200px; }
  .brand {
    position: absolute; left: 60px; top: 34px;
    display: flex; align-items: center; gap: 14px;
  }
  .brand-dot { width: 46px; height: 46px; border-radius: 50%; background: var(--paper); }
  .brand-name {
    font-family: "Lato", sans-serif; font-weight: 700;
    font-size: 36px; color: var(--paper); letter-spacing: 0.5px;
  }
  .globe-icon {
    position: absolute; left: 60px; top: 187px;
    width: 50px; height: 50px; border-radius: 50%;
    background: var(--brand-purple);
  }
  .person-icon {
    position: absolute; left: 594px; top: 190px;
    width: 42px; height: 38px;
    background: var(--brand-purple);
    border-radius: 18px 18px 4px 4px;
  }
  .offices { position: absolute; left: 99px; top: 227px; }
  .office-label { font-style: italic; font-size: 15px; line-height: 20px; }
  .office-address { font-weight: 500; font-size: 18px; line-height: 23px; }
  .office + .office { margin-top: 9px; }
  .contacts {
    position: absolute; right: 58px; top: 232px;
    text-align: right;
  }
  .contact-name { font-weight: 500; font-size: 20px; line-height: 27px; letter-spacing: 0.8px; }
  .contact-email { font-style: italic; font-size: 20px; line-height: 27px; letter-spacing: 1.2px; }
  .contact + .contact { margin-top: 17px; }
  .website {
    position: absolute; right: 58px; top: 382px;
    display: flex; align-items: center; gap: 6px;
    font-weight: 500; font-size: 17px; letter-spacing: 1px;
    color: var(--brand-red);
  }
</style>
</head>
<body>
  <div class="card">
    <svg class="card-header" viewBox="0 0 696 200" aria-hidden="true">
      <defs>
        <linearGradient id="headerGradient" x1="0" y1="0" x2="1" y2="0">
          <stop offset="0.15" stop-color="var(--brand-red)"/>
          <stop offset="0.45" stop-color="var(--brand-crimson)"/>
          <stop offset="0.85" stop-color="var(--brand-purple)"/>
        </linearGradient>
      </defs>
      <path fill="url(#headerGradient)"
        d="M0 0 H696 V68 C640 100 590 178 520 178 C450 178 390 120 268 122 C170 124 110 165 70 162 C40 160 30 130 0 124 Z"/>
    </svg>

    <div class="brand">
      <span class="brand-dot"></span>
      <span class="brand-name">VORTANI</span>
    </div>

    <div class="globe-icon" role="img" aria-label="Globe icon showing Europe and Africa"></div>
    <div class="person-icon" role="img" aria-label="Business person silhouette icon"></div>

    <div class="offices">
      <div class="office">
        <p class="office-label">Main office</p>
        <p class="office-address">Kornblumenweg 14<br>08352 Lindenfeld<br>Austria</p>
      </div>
      <div class="office">
        <p class="office-label">Branch office</p>
        <p class="office-address">Daska Lane<br>Karvanpur<br>Malaysia</p>
      </div>
    </div>

    <div class="contacts">
      <div class="contact">
        <p class="contact-name">Lukas Feldhaus (owner)</p>
        <p class="contact-email">lukas@vortani-example.com</p>
      </div>
      <div class="contact">
        <p class="contact-name">Imran Qureshi (owner)</p>
        <p class="contact-email">imran@vortani-example.com</p>
      </div>
    </div>

    <div class="website">
      <svg width="30" height="26" viewBox="0 0 30 26" aria-hidden="true">
        <circle cx="25" cy="4" r="3.5" fill="var(--brand-red)"/>
        <path fill="var(--brand-red)" d="M2 25 L6 12 L10 16 L18 8 L21 11 L13 19 L17 23 Z"/>
      </svg>
      <span>vortani-example.com</span>
    </div>
  </div>
</body>
</html>
```